Investment website design - investing in mutual funds

I need a design of a website (only homepage for now) dedicated to investment in mutual funds. Attached is a mock up with all the elements the homepage design should contain. The homepage should contain a logo in the upper left corner, the domain the website will run on is www.morvatelsko.cz , in the upper right corner there should be 2 buttons or links SIGN UP / SIGN IN. The bottom of the homepage should contain links to ABOUT US, FAQ, PRIVACY POLICY, CONTACT US.
Now the main elements on the homepage
1) Video that will explain how the investment works exactly, under this video we will have 3 illustrated icons like the ones attached (see 2nd attachement) that will show the potential investor what exactly they could get when investing with us (education for kids, happy life after they retire, regular monthly payment for the rest of their life).
2) On the right side next to the video we will have a calculator where a potential investor can play with the numbers, the investor can fill in the MONTHLY PAYMENT that he wants to invest regularly every month, the time frame of the investment - for how long he wants to invest. Once the potential investor selects those 2 variables we will calculate for him 2 options - either he can get a ONE TIME PAYOUT once he reaches his investment horizon or he can get a regular monthly payment for the rest of his life. Under the laculator there will be a button 'I want to invest ->'. The functionality of the calculator should be similar to the calculator that can be found here http://www.brovikbanka.cz/brovik-podilove-fondy/ and https://pelvaro.cz/.
The design should look similar to https://pelvaro.cz/ (font, colors, logo). We prefer white background in the area where we have the video and calculator. We also like the design of www.truvanex.com. Let me know if you have any questions.

```html
<!DOCTYPE html>
<html lang="en">
<head>
<meta charset="utf-8">
<title>Morvatelsko – Invest in Mutual Funds</title>
<link href="https://fonts.googleapis.com/css2?family=Lato:wght@400;700;900&display=swap" rel="stylesheet">
<style>
  :root {
    --teal: #2fa6b0;
    --ink: #3a3a3a;
    --muted: #555555;
    --field-border: #e6e6e6;
    --page: #fafafa;
    --white: #ffffff;
    --rule: #c8c8c8;
    --video-bg: #97bba6;
    --video-bar: #c42a25;
  }
  * { box-sizing: border-box; margin: 0; padding: 0; }
  html, body { width: 1200px; height: 665px; overflow: hidden; }
  body {
    background: var(--page);
    font-family: 'Lato', sans-serif;
    color: var(--ink);
    position: relative;
  }
  .brand {
    position: absolute; left: 101px; top: 27px;
    font-size: 31px; font-weight: 900; letter-spacing: 2px;
    color: var(--teal);
  }
  .auth { position: absolute; top: 29px; right: 100px; display: flex; gap: 22px; }
  .auth-btn {
    height: 33px; border-radius: 17px; border: 1px solid var(--teal);
    display: flex; align-items: center; justify-content: center; gap: 9px;
    font-size: 13px; font-weight: 700; text-decoration: none;
  }
  .auth-btn svg { width: 12px; height: 12px; }
  .auth-btn--in { width: 108px; background: var(--teal); color: var(--white); }
  .auth-btn--out { width: 118px; background: var(--white); color: var(--teal); }

  .video {
    position: absolute; left: 99px; top: 107px; width: 506px; height: 309px;
    background: var(--video-bg);
  }
  .video-progress { position: absolute; left: 50px; top: 290px; width: 329px; height: 7px; background: var(--white); }
  .video-progress span { display: block; width: 132px; height: 100%; background: var(--video-bar); }
  .video-play { position: absolute; left: 20px; top: 286px; width: 14px; height: 15px; }
  .video-full { position: absolute; right: 10px; top: 286px; width: 15px; height: 15px; }

  .benefits { position: absolute; left: 99px; top: 444px; width: 506px; }
  .benefit { position: absolute; top: 0; width: 170px; text-align: center; }
  .benefit-icon {
    width: 53px; height: 53px; border-radius: 50%; margin: 0 auto;
    border: 3px solid var(--white); box-shadow: 0 0 0 1px #e2e2e2;
  }
  .benefit-label { margin-top: 17px; font-size: 13px; font-weight: 700; color: var(--ink); white-space: nowrap; }

  .calculator { position: absolute; left: 653px; top: 100px; width: 448px; }
  .calculator h1 { font-size: 31px; font-weight: 700; letter-spacing: 0.2px; color: var(--ink); }
  .field {
    position: absolute; left: 0; width: 448px; height: 40px;
    background: var(--white); border: 1px solid var(--field-border);
    padding-left: 13px; display: flex; align-items: center;
    font-size: 11.5px; color: var(--muted);
  }
  .length-label { position: absolute; top: 116px; font-size: 15.5px; font-weight: 700; color: var(--ink); }
  .slider { position: absolute; top: 156px; left: 0; width: 448px; height: 7px; background: var(--teal); }
  .slider-handle { position: absolute; left: 33px; top: -4px; width: 12px; height: 16px; }
  .slider-scale { position: absolute; top: 183px; width: 448px; display: flex; justify-content: space-between; font-size: 13px; color: var(--muted); }
  .or { position: absolute; top: 268px; width: 448px; text-align: center; font-size: 13px; color: var(--muted); }
  .invest-btn {
    position: absolute; left: 282px; top: 374px; width: 166px; height: 35px;
    border-radius: 18px; background: var(--teal); color: var(--white);
    font-size: 13px; font-weight: 700; display: flex; align-items: center; justify-content: center;
    text-decoration: none;
  }

  .site-footer {
    position: absolute; left: 96px; top: 601px; width: 1004px;
    border-top: 1px solid var(--rule);
    display: flex; justify-content: space-between; padding: 24px 2px 0 5px;
    font-size: 12.5px; color: var(--ink);
  }
  .footer-nav { display: flex; }
  .footer-nav a { color: var(--ink); text-decoration: none; }
  .footer-nav .sep { margin: 0 30px; }
</style>
</head>
<body>
  <header>
    <div class="brand">MORVATELSKO</div>
    <nav class="auth">
      <a class="auth-btn auth-btn--in" href="#">
        <svg viewBox="0 0 12 12"><path d="M1 5h6V3l3 3-3 3V7H1z" fill="currentColor"/><path d="M7 1h4v10H7" fill="none" stroke="currentColor" stroke-width="1.4"/></svg>SIGN-IN</a>
      <a class="auth-btn auth-btn--out" href="#">
        <svg viewBox="0 0 12 12"><path d="M1 5h6V3l3 3-3 3V7H1z" fill="currentColor"/><path d="M7 1h4v10H7" fill="none" stroke="currentColor" stroke-width="1.4"/></svg>SIGN-OUT</a>
    </nav>
  </header>

  <main>
    <section class="video" role="img" aria-label="Explainer video illustration: two women exchanging a money bag and a light bulb, with circular arrows between them">
      <svg class="video-play" viewBox="0 0 14 15"><path d="M1 1l12 6.5L1 14z" fill="#fff"/></svg>
      <div class="video-progress"><span></span></div>
      <svg class="video-full" viewBox="0 0 15 15" fill="none" stroke="#fff" stroke-width="2">
        <path d="M1 5V1h4M10 1h4v4M14 10v4h-4M5 14H1v-4"/>
      </svg>
    </section>

    <section class="benefits">
      <div class="benefit" style="left:-13px">
        <div class="benefit-icon" role="img" aria-label="Illustration of a graduation cap on stacked books" style="background:#8cc0d6"></div>
        <div class="benefit-label">EDUCATION FOR KIDS</div>
      </div>
      <div class="benefit" style="left:171px">
        <div class="benefit-icon" role="img" aria-label="Illustration of a hand dropping a coin into a piggy bank" style="background:#9fd0e6"></div>
        <div class="benefit-label">PASSIVE INCOME</div>
      </div>
      <div class="benefit" style="left:355px">
        <div class="benefit-icon" role="img" aria-label="Illustration of an elderly couple" style="background:#f2ede4"></div>
        <div class="benefit-label">HAPPY RETIREMENT</div>
      </div>
    </section>

    <section class="calculator">
      <h1>OUR ONLINE CALCULATOR</h1>
      <div class="field" style="top:55px">Regular Monthly Investment</div>
      <div class="length-label">Length of investment</div>
      <div class="slider">
        <svg class="slider-handle" viewBox="0 0 12 16"><path d="M0 0h12v11l-6 5-6-5z" fill="#333"/></svg>
      </div>
      <div class="slider-scale"><span>0</span><span>30 Years</span></div>
      <div class="field" style="top:210px">One time payout</div>
      <div class="or">(or)</div>
      <div class="field" style="top:302px">Monthly payment</div>
      <a class="invest-btn" href="#">I WANT TO INVEST &gt;&gt;</a>
    </section>
  </main>

  <footer class="site-footer">
    <nav class="footer-nav">
      <a href="#">About Us</a><span class="sep">|</span>
      <a href="#">FAQ</a><span class="sep">|</span>
      <a href="#">Privacy Policy</a><span class="sep">|</span>
      <a href="#">Contact</a>
    </nav>
    <div class="copyright">Copyrights © 2017 Morvatelsko . Allrights Reserved</div>
  </footer>
</body>
</html>
```